General Power Point Presentation Pack

Hello Designers,

I am after a professional looking Microsoft PowerPoint deck that can be used for our corporate presentations. The pack should include a:

Title Page
Tittle and Content Page
Section Header Sheet
Two Content Page
Title Only Page
Blank Page
Content with Caption Page
Picture with Caption Page

I have included my brand guidelines and colours. I have also included some photos you may be able to use. Can you please ensure the pack has page numbering and that when you print it that it can be printed to full A4 Page.

Industry/Entity Type

Property Development & Construction

Requirements
Must have
• Prefer a white or very light coloured background

```html
<!DOCTYPE html>
<html lang="en">
<head>
<meta charset="utf-8">
<title>Halden – Presentation Pack</title>
<link href="https://fonts.googleapis.com/css2?family=Roboto:wght@400;500;700&display=swap" rel="stylesheet">
<style>
:root{
  --page:#f2f2f2;
  --white:#ffffff;
  --gold:#c9a05c;
  --gold-dark:#9c7440;
  --gold-light:#e3c48a;
  --grey:#6a6a6a;
  --ink:#2b2b2b;
  --cream:#f3ebdd;
  --cream-faint:#f5ede2;
  --orange:#d95f2b;
  --teal:#6fb3a1;
  --panel:rgba(40,40,40,.72);
}
*{margin:0;padding:0;box-sizing:border-box}
html,body{width:1200px;height:2983px;overflow:hidden;background:var(--page);font-family:"Roboto",Arial,sans-serif;color:var(--grey)}
.canvas{position:relative;width:1200px;height:2983px}
.slide{position:absolute;width:540px;height:382px;overflow:hidden;background:var(--white)}
.col-l{left:47px}.col-r{left:613px}
.row1{top:51px}.row2{top:456px}.row3{top:861px}.row4{top:1266px}.row5{top:1671px}.row6{top:2077px}.row7{top:2482px}
.abs{position:absolute}
.gold-bar{position:absolute;left:0;bottom:0;width:100%;height:7px;background:linear-gradient(90deg,var(--gold-dark),var(--gold-light) 50%,var(--gold-dark))}
.framed{border:7px solid var(--gold-dark);border-image:linear-gradient(90deg,var(--gold-dark),var(--gold-light),var(--gold-dark)) 1}
.page-no{position:absolute;right:22px;bottom:14px;width:22px;height:22px;border-radius:50%;border:1px solid #8a8a8a;background:var(--white);font-size:8px;color:var(--ink);display:flex;align-items:center;justify-content:center}
.page-no.ghost{background:transparent;border-color:rgba(255,255,255,.6);color:rgba(255,255,255,.7)}
/* photos */
.photo{position:absolute}
.ph-ext{background:linear-gradient(180deg,#a9bccb 0%,#d9d4c8 40%,#b9a98e 65%,#4e5648 100%)}
.ph-dusk{background:linear-gradient(180deg,#3e4a63 0%,#7d6d73 40%,#6b5a4d 70%,#2c3328 100%)}
.ph-int{background:linear-gradient(180deg,#e9e4dc 0%,#d8ccba 55%,#b69a78 100%)}
.ph-warm{background:linear-gradient(180deg,#ece6dc 0%,#e2cfb4 50%,#c07a45 80%,#b89a74 100%)}
.ph-mod{background:linear-gradient(160deg,#d9dde0 0%,#9a8c7c 50%,#3f3b37 100%)}
.ph-site{background:linear-gradient(160deg,#e8d27a 0%,#f2c300 40%,#a9a9a2 100%)}
.ph-sky{background:linear-gradient(180deg,#7ba4cf 0%,#b9cde0 60%,#8b8f92 100%)}
.ph-dig{background:linear-gradient(180deg,#e9d8b6 0%,#d7a93a 50%,#8c7556 100%)}
/* brand */
.brand{position:absolute;display:flex;align-items:center;gap:5px;font-size:15px;font-weight:500;color:var(--gold);letter-spacing:.3px}
.brand-sq{width:9px;height:9px;background:currentColor}
.brand.light{color:var(--white)}
.brand.faint{color:rgba(201,160,92,.45)}
/* type */
.h-title{position:absolute;font-size:15px;font-weight:500;color:var(--grey);letter-spacing:.3px}
.h-title .g{color:var(--gold)}
.h-title.light{color:var(--white)}
.edge-mark{position:absolute;left:0;width:3px;height:15px;background:var(--gold)}
.body{position:absolute;font-size:8px;line-height:1.45;color:var(--grey)}
.body.light{color:var(--white)}
.body p+p{margin-top:7px}
.body b{color:var(--ink);font-weight:500;display:block}
.bullets{list-style:none}
.bullets li{position:relative;padding-left:13px;margin-bottom:11px}
.bullets li::before{content:"";position:absolute;left:0;top:3px;width:5px;height:5px;border-radius:50%;background:var(--gold)}
/* toc */
.toc{position:absolute;left:300px;top:160px;width:190px;list-style:none;font-size:8px;color:var(--white)}
.toc li{height:26px;padding-top:7px;border-bottom:1px solid rgba(255,255,255,.35)}
/* cards */
.card{position:absolute;top:145px;width:153px;height:205px;background:var(--cream)}
.card::after{content:"";position:absolute;left:0;bottom:0;width:100%;height:4px;background:var(--gold)}
.card-icon{position:absolute;left:58px;top:12px;width:36px;height:36px;border-radius:50%}
.card .body{left:14px;top:63px;width:125px;text-align:center}
/* features */
.feature{position:absolute;top:115px;width:130px}
.feature-img{position:relative;height:90px}
.tag{position:absolute;left:-6px;bottom:6px;background:var(--orange);color:var(--white);font-size:6px;padding:2px 10px}
.feature h4{font-size:7px;font-weight:700;color:var(--ink);margin-top:10px;line-height:1.3}
.feature .body{position:static;margin-top:9px;font-size:6.5px}
.btn{display:inline-block;margin-top:12px;width:92px;background:var(--gold);color:var(--white);font-size:7px;text-align:center;padding:4px 0}
/* contact */
.contact-row{position:absolute;left:60px;display:flex;align-items:center;gap:11px;font-size:10px;color:var(--white)}
.social{position:absolute;left:60px;top:320px;display:flex;gap:9px}
.social span{width:16px;height:16px;border-radius:50%;background:var(--gold)}
</style>
</head>
<body>
<main class="canvas">

<!-- 01 Title page -->
<section class="slide col-l row1">
  <div class="photo ph-ext" style="left:0;top:0;width:540px;height:280px" role="img" aria-label="Photograph of a modern white and timber apartment complex"></div>
  <div class="brand" style="left:42px;top:325px">Halden</div>
  <div class="abs" style="left:143px;top:305px;width:1px;height:40px;background:#c9c9c9"></div>
  <div class="abs" style="left:164px;top:303px;font-size:19px;font-weight:500;color:var(--gold)">LOREM IPSUM DOLOR SIT AMET</div>
  <div class="abs" style="left:164px;top:333px;font-size:8px;font-weight:500;color:var(--ink)">LOREM IPSUM DOLOR SIT AMET CONSECTETUER ADIPISCING ELIT SED</div>
</section>

<!-- 02 Section header -->
<section class="slide col-r row1 framed">
  <div class="photo ph-sky" style="inset:0" role="img" aria-label="Photograph of a dark glass apartment building on a street corner"></div>
  <div class="brand light" style="left:35px;top:205px;font-size:22px">Halden</div>
  <div class="h-title light" style="left:35px;top:255px;font-size:18px">LOREM IPSUM DOLOR</div>
  <div class="body light" style="left:35px;top:300px;width:280px;font-size:9px;line-height:1.3">Lorem ipsum dolor sit amet, consectetuer adipiscing elit, sed diam nonummy nibh euismod tincidunt ut laoreet dolore magna aliquam erat volutpat. Ut wisi enim ad minim veniam.</div>
</section>

<!-- 03 Table of content -->
<section class="slide col-l row2">
  <div class="photo ph-dusk" style="inset:0" role="img" aria-label="Evening photograph of an apartment entrance with palm trees"></div>
  <div class="abs" style="left:271px;top:0;width:269px;height:382px;background:rgba(40,42,50,.55)"></div>
  <div class="brand" style="left:358px;top:60px">Halden</div>
  <div class="abs" style="left:300px;top:113px;font-size:15px;font-weight:500;color:var(--white)">TABLE OF <span style="color:var(--gold)">CONTENT</span></div>
  <ul class="toc">
    <li>Market Overview</li><li>Concept</li><li>Experience Packages</li><li>Experience Formula</li><li>Team Formula</li><li>Loyalty Formula</li><li>Who We Are</li>
  </ul>
  <div class="page-no ghost" style="right:42px">02</div>
  <div class="gold-bar"></div>
</section>

<!-- 04 Title and content -->
<section class="slide col-r row2">
  <div class="brand" style="left:42px;top:65px">Halden</div>
  <span class="edge-mark" style="top:111px"></span>
  <div class="h-title" style="left:42px;top:113px">LOREM <span class="g">IPSUM DOLOR</span></div>
  <ul class="body bullets" style="left:42px;top:158px;width:225px">
    <li>Lorem ipsum dolor sit amet, consectetuer adipiscing elit, sed diam nonummy nibh euismod tincidunt ut laoreet dolore magna aliquam volutpat. Ut wisi enim ad minim veniam, quis nostrud exerci tation</li>
    <li>Lorem ipsum dolor sit amet, consectetuer adipiscing elit, sed diam nonummy nibh euismod tincidunt ut laoreet dolore magna aliquam volutpat. Ut wisi enim ad minim veniam, quis nostrud exerci tation</li>
    <li>Lorem ipsum dolor sit amet, consectetuer adipiscing elit, sed diam nonummy nibh euismod tincidunt ut laoreet dolore magna aliquam volutpat. Ut wisi enim ad minim veniam, quis nostrud exerci tation</li>
  </ul>
  <div class="photo ph-int" style="left:294px;top:60px;width:206px;height:262px" role="img" aria-label="Photograph of a dining room interior with wooden chairs"></div>
  <div class="page-no">03</div>
  <div class="gold-bar"></div>
</section>

<!-- 05 Content with picture -->
<section class="slide col-l row3">
  <div class="brand" style="left:42px;top:65px">Halden</div>
  <span class="edge-mark" style="top:111px"></span>
  <div class="h-title" style="left:42px;top:113px">LOREM <span class="g">IPSUM DOLOR</span></div>
  <div class="body" style="left:42px;top:158px;width:205px">Lorem ipsum dolor sit amet, consectetuer adipiscing elit, sed diam nonummy nibh euismod tincidunt ut laoreet dolore magna aliquam erat volutpat. Ut wisi enim ad minim veniam, quis nostrud exerci tation ullamcorper suscipit lobortis nisl ut aliquip ex ea commodo consequat. Duis autem vel eum iriure dolor in hendrerit in vulputate velit esse molestie consequat, vel illum dolore eu feugiat nulla facilisis at vero eros et accumsan et iusto odio dignissim qui blandit praesent luptatum</div>
  <div class="body" style="left:42px;top:290px;width:205px;color:var(--gold)">Lorem ipsum dolor sit amet, consectetuer adipiscing elit, sed diam nonummy nibh euismod</div>
  <div class="photo ph-mod" style="left:280px;top:0;width:260px;height:375px" role="img" aria-label="Photograph of a timber and glass building with a pergola and steps"></div>
  <div class="page-no ghost" style="right:42px">04</div>
  <div class="gold-bar"></div>
</section>

<!-- 06 Three cards -->
<section class="slide col-r row3">
  <div class="photo ph-int" style="left:0;top:0;width:540px;height:175px" role="img" aria-label="Photograph of a bright living and dining interior"></div>
  <div class="abs" style="left:0;top:0;width:540px;height:115px;background:linear-gradient(90deg,rgba(40,40,40,.7),rgba(40,40,40,.25))"></div>
  <span class="edge-mark" style="top:58px"></span>
  <div class="h-title light" style="left:42px;top:60px">LOREM <span class="g">IPSUM DOLOR</span></div>
  <div class="body light" style="left:42px;top:85px;width:290px">Lorem ipsum dolor sit amet, consectetuer adipiscing elit, sed diam nonummy nibh euismod tincidunt ut laoreet dolore magna aliquam erat</div>
  <div class="brand faint" style="left:415px;top:66px">Halden</div>
  <div class="card" style="left:22px">
    <svg class="card-icon" viewBox="0 0 36 36" style="background:var(--orange)"><ellipse cx="18" cy="18" rx="10" ry="6" fill="none" stroke="#fff" stroke-width="1.5"/><circle cx="18" cy="18" r="3" fill="#fff"/></svg>
    <div class="body">Lorem ipsum dolor sit amet, consectetuer adipiscing elit, sed diam nonummy nibh euismod tincidunt ut laoreet dolore magna aliquam erat volutpat. Ut wisi enim ad minim veniam, quis nostrud exerci tation ullamcorper suscipit lobortis nisl ut aliquip ex ea commodo</div>
  </div>
  <div class="card" style="left:193px">
    <svg class="card-icon" viewBox="0 0 36 36" style="background:var(--teal)"><circle cx="18" cy="18" r="9" fill="none" stroke="#fff" stroke-width="1.5"/><circle cx="18" cy="18" r="5" fill="none" stroke="#fff" stroke-width="1.5"/><circle cx="18" cy="18" r="1.5" fill="#fff"/></svg>
    <div class="body">Lorem ipsum dolor sit amet, consectetuer adipiscing elit, sed diam nonummy nibh euismod tincidunt ut laoreet dolore magna aliquam erat volutpat. Ut wisi enim ad minim veniam, quis nostrud exerci tation ullamcorper suscipit lobortis nisl ut aliquip ex ea commodo</div>
  </div>
  <div class="card" style="left:366px">
    <svg class="card-icon" viewBox="0 0 36 36" style="background:var(--orange)"><circle cx="18" cy="16" r="6" fill="none" stroke="#fff" stroke-width="1.5"/><path d="M15 24h6M16 27h4M18 6v2M8 16h2M26 16h2" stroke="#fff" stroke-width="1.5"/></svg>
    <div class="body">Lorem ipsum dolor sit amet, consectetuer adipiscing elit, sed diam nonummy nibh euismod tincidunt ut laoreet dolore magna aliquam erat volutpat. Ut wisi enim ad minim veniam, quis nostrud exerci tation ullamcorper suscipit lobortis nisl ut aliquip ex ea commodo</div>
  </div>
  <div class="page-no">05</div>
  <div class="gold-bar"></div>
</section>

<!-- 07 Two content -->
<section class="slide col-l row4">
  <span class="edge-mark" style="top:56px"></span>
  <div class="h-title" style="left:42px;top:58px">LOREM <span class="g">IPSUM DOLOR</span></div>
  <div class="brand" style="left:415px;top:68px">Halden</div>
  <div class="body" style="left:42px;top:118px;width:215px;font-size:7px">
    <p><b>Lorem ipsum dolor sit amet, consectetuer</b>Diam nonummy nibh euismod tincidunt ut laoreet dolore magna aliquam erat volutpat. Ut wisi enim ad minim veniam, quis nostrud exerci tation ullamcorper suscipit lobortis nisl ut aliquip ex ea commodo consequat.</p>
    <p><b>Duis autem vel eum iriure dolor in hendrerit in</b>Vulputate velit esse molestie consequat, vel illum dolore eu feugiat nulla facilisis at vero eros et accumsan et iusto odio dignissim qui blandit praesent luptatum zzril delenit augue duis dolore te feugait nulla facilisi.</p>
    <p><b>Lorem ipsum dolor sit amet</b>Cons ectetuer adipiscing elit, sed diam nonummy nibh euismod tincidunt ut laoreet dolore magna aliquam erat volutpat. Ut wisi enim ad minim veniam, quis nostrud exerci tation ullamcorper suscipit lobortis nisl ut aliquip ex ea</p>
  </div>
  <div class="body" style="left:283px;top:118px;width:215px;font-size:7px">
    <p><b>Lorem ipsum dolor sit amet, consectetuer</b>Diam nonummy nibh euismod tincidunt ut laoreet dolore magna aliquam erat volutpat. Ut wisi enim ad minim veniam, quis nostrud exerci tation ullamcorper suscipit lobortis nisl ut aliquip ex ea commodo consequat.</p>
    <p><b>Duis autem vel eum iriure dolor in hendrerit in</b>Vulputate velit esse molestie consequat, vel illum dolore eu feugiat nulla facilisis at vero eros et accumsan et iusto odio dignissim qui blandit praesent luptatum zzril delenit augue duis dolore te feugait nulla facilisi.</p>
    <p><b>Lorem ipsum dolor sit amet</b>Cons ectetuer adipiscing elit, sed diam nonummy nibh euismod tincidunt ut laoreet dolore magna aliquam erat volutpat. Ut wisi enim ad minim veniam, quis nostrud exerci tation ullamcorper suscipit lobortis nisl ut aliquip ex ea</p>
  </div>
  <div class="page-no">06</div>
  <div class="gold-bar"></div>
</section>

<!-- 08 Picture with panels -->
<section class="slide col-r row4">
  <div class="photo ph-sky" style="left:0;top:0;width:180px;height:375px" role="img" aria-label="Photograph looking up at a balconied apartment building and trees"></div>
  <div class="abs" style="left:180px;top:0;width:180px;height:375px;background:#3d3d3f"></div>
  <div class="abs" style="left:360px;top:0;width:180px;height:375px;background:var(--gold)"></div>
  <div class="brand" style="left:225px;top:50px">Halden</div>
  <div class="abs" style="left:211px;top:92px;font-size:11px;font-weight:500;color:var(--white)">LOREM IPSUM DOLOR</div>
  <div class="body light" style="left:211px;top:112px;width:130px;line-height:1.4">Lorem ipsum dolor sit amet, consectetuer adipiscing elit, sed diam nonummy nibh euismod tincidunt ut laoreet dolore magna aliquam erat volutpat. Ut wisi enim ad minim veniam, quis nostrud exerci tation ullamcorper suscipit lobortis nisl ut aliquip ex ea commodo consequat. Duis autem vel eum iriure dolor in hendrerit in vulputate velit esse molestie consequat, vel illum dolore eu feugiat nulla facilisis at vero eros et accumsan et iusto odio dignissim qui blandit praesent luptatum zzril delenit augue duis dolore te feugait nulla</div>
  <div class="abs" style="left:388px;top:92px;font-size:11px;font-weight:500;color:var(--white)">LOREM IPSUM DOLOR</div>
  <div class="body light" style="left:388px;top:112px;width:130px;line-height:1.4">Lorem ipsum dolor sit amet, consectetuer adipiscing elit, sed diam nonummy nibh euismod tincidunt ut laoreet dolore magna aliquam erat volutpat. Ut wisi enim ad minim veniam, quis nostrud exerci tation ullamcorper suscipit lobortis nisl ut aliquip ex ea commodo consequat. Duis autem vel eum iriure dolor in hendrerit in vulputate velit esse molestie consequat, vel illum dolore eu feugiat nulla facilisis at vero eros et accumsan et iusto odio dignissim qui blandit praesent luptatum zzril delenit augue duis dolore te feugait nulla</div>
  <div class="page-no ghost">07</div>
  <div class="gold-bar"></div>
</section>

<!-- 09 Title only -->
<section class="slide col-l row5">
  <span class="edge-mark" style="top:56px"></span>
  <div class="h-title" style="left:42px;top:58px">LOREM <span class="g">IPSUM DOLOR</span></div>
  <div class="brand" style="left:415px;top:68px">Halden</div>
  <div class="abs" style="left:325px;top:105px;width:180px;height:232px;background:var(--cream-faint)"></div>
  <div class="page-no">08</div>
  <div class="gold-bar"></div>
</section>

<!-- 10 Three features -->
<section class="slide col-r row5">
  <span class="edge-mark" style="top:56px"></span>
  <div class="h-title" style="left:42px;top:58px">LOREM <span class="g">IPSUM DOLOR</span></div>
  <div class="brand" style="left:415px;top:68px">Halden</div>
  <div class="feature" style="left:42px">
    <div class="feature-img ph-int" role="img" aria-label="Photograph of a living room interior"><span class="tag">Lorem ipsum</span></div>
    <h4>LOREM IPSUM DOLOR SIT AMET CONSECTETUER ADIPISCING</h4>
    <div class="body">Lorem ipsum dolor sit amet, consectetuer adipiscing elit, sed diam nonummy nibh euismod tincidunt ut laoreet dolore magna aliquam erat</div>
    <span class="btn">Lorem ipsum</span>
  </div>
  <div class="feature" style="left:205px">
    <div class="feature-img ph-warm" role="img" aria-label="Photograph of a bedroom interior"><span class="tag">Lorem ipsum</span></div>
    <h4>LOREM IPSUM DOLOR SIT AMET CONSECTETUER ADIPISCING</h4>
    <div class="body">Lorem ipsum dolor sit amet, consectetuer adipiscing elit, sed diam nonummy nibh euismod tincidunt ut laoreet dolore magna aliquam erat</div>
    <span class="btn">Lorem ipsum</span>
  </div>
  <div class="feature" style="left:368px">
    <div class="feature-img ph-int" role="img" aria-label="Photograph of a kitchen interior with stools"><span class="tag">Lorem ipsum</span></div>
    <h4>LOREM IPSUM DOLOR SIT AMET CONSECTETUER ADIPISCING</h4>
    <div class="body">Lorem ipsum dolor sit amet, consectetuer adipiscing elit, sed diam nonummy nibh euismod tincidunt ut laoreet dolore magna aliquam erat</div>
    <span class="btn">Lorem ipsum</span>
  </div>
  <div class="page-no">09</div>
  <div class="gold-bar"></div>
</section>

<!-- 11 Picture with caption -->
<section class="slide col-l row6">
  <div class="photo ph-warm" style="inset:0" role="img" aria-label="Photograph of a living room with an orange sofa and timber screen"></div>
  <div class="brand" style="left:42px;top:55px">Halden</div>
  <div class="abs" style="left:15px;top:90px;width:265px;height:90px;background:var(--panel)"></div>
  <span class="edge-mark" style="top:112px"></span>
  <div class="h-title light" style="left:42px;top:114px">LOREM <span class="g">IPSUM DOLOR</span></div>
  <div class="body light" style="left:42px;top:138px;width:220px">Lorem ipsum dolor sit amet, consectetuer adipiscing elit, sed diam nonummy nibh euismod tincidunt ut</div>
  <div class="page-no ghost" style="right:42px">10</div>
  <div class="gold-bar"></div>
</section>

<!-- 12 Content with pictures -->
<section class="slide col-r row6">
  <div class="photo ph-site" style="left:0;top:0;width:345px;height:187px" role="img" aria-label="Photograph of a tape measure, hard hat and building plans"></div>
  <div class="photo ph-sky" style="left:352px;top:0;width:188px;height:187px" role="img" aria-label="Photograph of construction cranes against a blue sky"></div>
  <div class="photo ph-dig" style="left:352px;top:195px;width:188px;height:180px" role="img" aria-label="Photograph of an excavator on a construction site at sunset"></div>
  <div class="brand" style="left:42px;top:215px">Halden</div>
  <span class="edge-mark" style="top:250px"></span>
  <div class="h-title" style="left:42px;top:252px">LOREM <span class="g">IPSUM DOLOR</span></div>
  <div class="body" style="left:42px;top:282px;width:290px">Lorem ipsum dolor sit amet, consectetuer adipiscing elit, sed diam nonummy nibh euismod tincidunt ut laoreet dolore magna aliquam erat volutpat. Ut wisi enim ad minim veniam, quis nostrud exerci tation ullamcorper suscipit lobortis nisl ut aliquip ex ea commodo consequat.</div>
  <div class="page-no ghost">11</div>
  <div class="gold-bar"></div>
</section>

<!-- 13 Gallery -->
<section class="slide col-l row7">
  <div class="photo ph-sky" style="left:0;top:0;width:172px;height:375px" role="img" aria-label="Photograph of an apartment building behind trees"></div>
  <div class="photo ph-ext" style="left:183px;top:0;width:357px;height:195px" role="img" aria-label="Photograph of a white and timber apartment complex"></div>
  <div class="photo ph-dusk" style="left:183px;top:205px;width:172px;height:170px" role="img" aria-label="Evening photograph of an apartment entrance with palm trees"></div>
  <div class="photo ph-int" style="left:365px;top:205px;width:175px;height:170px" role="img" aria-label="Photograph of a lounge interior with armchairs"></div>
  <div class="page-no ghost">12</div>
  <div class="gold-bar"></div>
</section>

<!-- 14 Contact -->
<section class="slide col-r row7 framed">
  <div class="photo ph-ext" style="inset:0" role="img" aria-label="Photograph of a modern apartment complex with timber screens"></div>
  <div class="abs" style="left:0;top:0;width:300px;height:100%;background:linear-gradient(90deg,rgba(30,30,30,.55),rgba(30,30,30,0))"></div>
  <div class="brand" style="left:53px;top:148px">Halden</div>
  <div class="abs" style="left:53px;top:180px;font-size:24px;font-weight:500;color:var(--white)">CONTACT US</div>
  <div class="contact-row" style="left:53px;top:225px">
    <svg width="14" height="10" viewBox="0 0 14 10"><rect x=".5" y=".5" width="13" height="9" fill="none" stroke="#fff"/><path d="M.5 .5 7 6 13.5 .5" fill="none" stroke="#fff"/></svg>
    <span>Lorem ipsum dolor sit amet</span>
  </div>
  <div class="contact-row" style="left:53px;top:252px">
    <svg width="14" height="14" viewBox="0 0 14 14"><rect x="3.5" y=".5" width="7" height="13" rx="1" fill="none" stroke="#fff"/><circle cx="7" cy="11" r=".8" fill="#fff"/></svg>
    <span>Lorem ipsum dolor sit amet</span>
  </div>
  <div class="contact-row" style="left:53px;top:279px">
    <svg width="14" height="14" viewBox="0 0 14 14"><circle cx="7" cy="7" r="6.2" fill="none" stroke="#fff"/><ellipse cx="7" cy="7" rx="2.8" ry="6.2" fill="none" stroke="#fff"/><path d="M1 7h12" stroke="#fff"/></svg>
    <span>Lorem ipsum dolor sit amet</span>
  </div>
  <div class="social" style="left:53px;top:310px"><span></span><span></span><span></span></div>
</section>

</main>
</body>
</html>
```